PIETRO business card - High end Italian floors and coverings

We need a new design for our business card. We are an exclusive company located in Mexico.
Our commercial name is PIETRO. Our legal name is Grande Volta SA de CV.
We bring the latest trends in materials for floors and walls such as natural stones, wood, leather, design porcelanato tiles and so.
Our company image colors are black, white and red.
Our customers are high end architects and designers.
We are looking for an elegant but fresh design which reflects exclusivity, simplicity and reliability.
(we are working also in a new website)

Requirements
Nice to have
• back and front design
Space for 2 addresses (one for each showroom location)

```html
<!DOCTYPE html>
<html lang="es">
<head>
<meta charset="utf-8">
<title>PIETRO – Tarjetas de presentación</title>
<link rel="stylesheet" href="https://fonts.googleapis.com/css2?family=Questrial&family=Montserrat:wght@700&display=swap">
<style>
  :root {
    --backdrop: #e4e4e4;
    --card-light: #ffffff;
    --card-dark: #3a3a3c;
    --ink-dark: #2a2a2a;
    --ink-light: #e9e9e9;
    --accent: #d50f0f;
  }
  * { box-sizing: border-box; margin: 0; padding: 0; }
  html, body { width: 1200px; height: 800px; overflow: hidden; }
  body {
    background: var(--backdrop);
    font-family: "Questrial", "Century Gothic", sans-serif;
  }
  .sheet {
    position: relative;
    width: 1200px;
    height: 800px;
  }
  .card {
    position: absolute;
    top: 245px;
    width: 540px;
    height: 310px;
    box-shadow: 0 6px 18px rgba(0,0,0,0.18);
  }
  .card--front { left: 40px; background: var(--card-light); color: var(--ink-dark); }
  .card--back  { left: 620px; background: var(--card-dark); color: var(--ink-light); }

  .brand {
    position: absolute;
    top: 34px;
    right: 34px;
    display: flex;
    align-items: center;
    gap: 12px;
  }
  .brand__square {
    width: 30px;
    height: 30px;
    background: var(--accent);
  }
  .brand__name {
    font-family: "Questrial", "Century Gothic", sans-serif;
    font-size: 34px;
    letter-spacing: 3px;
    line-height: 1;
    color: var(--accent);
  }

  .person { position: absolute; left: 40px; }
  .card--front .person { top: 84px; }
  .card--back .person { top: 222px; }
  .person__name {
    font-family: "Montserrat", "Century Gothic", sans-serif;
    font-weight: 700;
    font-size: 19px;
    letter-spacing: 0.3px;
  }
  .person__email { font-size: 15px; margin-top: 3px; }

  .label { color: var(--accent); }

  .address {
    position: absolute;
    left: 40px;
    font-size: 14.5px;
    line-height: 1.35;
  }
  .card--front .address { top: 228px; }
  .card--back .address { top: 150px; }
</style>
</head>
<body>
<main class="sheet">

  <section class="card card--front" aria-label="Frente de la tarjeta">
    <div class="brand">
      <span class="brand__square"></span>
      <span class="brand__name">PIETRO</span>
    </div>
    <div class="person">
      <p class="person__name">MARTA REYES OLIVERI</p>
      <p class="person__email"><span class="label">Email:</span> marta@pietro.com.mx</p>
    </div>
    <address class="address" style="font-style:normal">
      Cristal #1480 Esq. Lyon, Colonia Moderna CP 44190<br>
      Guadalajara, Jalisco · <span class="label">Tel:</span> (33) 300.412.08
    </address>
  </section>

  <section class="card card--back" aria-label="Reverso de la tarjeta">
    <div class="brand">
      <span class="brand__square"></span>
      <span class="brand__name">PIETRO</span>
    </div>
    <address class="address" style="font-style:normal">
      Lago Ness #240 Local B 1er piso, Colonia<br>
      Granada CP 11500, Mexico, DF · <span class="label">Tel:</span> (33) 500.218.64
    </address>
    <div class="person">
      <p class="person__name">MARTA REYES OLIVERI</p>
      <p class="person__email"><span class="label">Email:</span> marta@pietro.com.mx</p>
    </div>
  </section>

</main>
</body>
</html>
```